Extra job from Lorvane Logo design job

This posting is for the winner of the Lorvane Swim Shop logo, we need an example of what the commerce webpage would look like.

Please go here to submit the logo first:

http://jobs.pixelmarquee.com/job.aspx?id=512807.

Shop

```html
<!DOCTYPE html>
<html lang="en">
<head>
<meta charset="utf-8">
<title>Lorvane Swim Shop</title>
<link rel="stylesheet" href="https://fonts.googleapis.com/css2?family=Montserrat:wght@400;500;600;700&family=Oswald:wght@300;400&family=Sacramento&display=swap">
<style>
:root{
  --orange:#f15a24;
  --green:#6db33f;
  --blue-text:#1a9ad6;
  --ink:#333;
  --heading:#4a4a4a;
  --panel:#e6e5dd;
  --footer:#30535f;
  --white:#fff;
  --line:#9a9a9a;
}
*{box-sizing:border-box;margin:0;padding:0}
html,body{width:1200px;height:1170px;overflow:hidden;background:var(--white)}
body{position:relative;font-family:Arial,Helvetica,sans-serif;color:var(--ink)}
h1,h2{font-weight:400}
.abs{position:absolute}

.brand{left:275px;top:82px;display:flex;align-items:center;gap:12px}
.brand-dot{width:34px;height:34px;border-radius:50%;background:var(--orange)}
.brand-name{font-family:'Montserrat',sans-serif;font-weight:600;font-size:22px;color:var(--orange)}

.header-login{left:663px;top:91px;font-family:'Montserrat',sans-serif;font-weight:600;font-size:13px;color:var(--orange);letter-spacing:.5px}
.search{left:744px;top:77px;width:312px;height:41px;border:1px solid #bbb;padding:8px 20px;font-family:'Oswald',sans-serif;font-weight:300;font-size:18px;color:#999}
.search-icon{left:1059px;top:83px}

.nav{left:0;top:203px;width:1200px;height:35px;background:var(--orange);border-bottom:1px solid #f7a07e}
.nav a{position:absolute;top:9px;font-family:'Montserrat',sans-serif;font-weight:500;font-size:15px;letter-spacing:1px;color:var(--white);text-decoration:none}

.hero{left:0;top:238px;width:1200px;height:373px;background:linear-gradient(180deg,#2f78b5 0%,#3a7fb7 55%,#1f5a86 68%,#1c7e88 84%,#d9e5e6 100%)}
.hero-title{left:212px;top:262px;font-family:'Sacramento',cursive;font-size:62px;color:var(--white);text-shadow:0 2px 8px rgba(0,0,0,.35)}
.btn{background:var(--green);color:var(--white);font-family:'Oswald',sans-serif;font-weight:400;text-align:center;border-radius:2px}
.shop-now{left:207px;top:359px;width:144px;height:46px;line-height:46px;font-size:19px}

.welcome-photo{left:62px;top:654px;width:269px;height:171px;background:linear-gradient(180deg,#8fb9dc 0%,#cfe0ea 45%,#4fb0b5 62%,#e3d8c4 80%)}
.welcome-title{left:365px;top:654px;font-family:'Montserrat',sans-serif;font-weight:400;font-size:22px;color:var(--heading)}
.welcome-lead{left:365px;top:682px;width:420px;font-family:'Montserrat',sans-serif;font-weight:500;font-size:13.5px;line-height:22px;color:var(--blue-text)}
.welcome-body{left:365px;top:735px;width:448px;font-size:12px;line-height:20px;text-align:justify;color:var(--ink)}
.divider-v{left:842px;top:645px;height:183px;border-left:1px dotted var(--line)}

.login-panel{left:873px;top:639px;width:300px;height:196px;background:var(--panel)}
.login-title{left:33px;top:17px;font-family:'Montserrat',sans-serif;font-weight:400;font-size:22px;color:var(--heading)}
.field-label{left:29px;font-size:12.5px;color:#222}
.field{left:105px;width:160px;height:27px;background:var(--white);border:1px solid #c8c8c8}
.login-btn{left:107px;top:140px;width:79px;height:32px;line-height:32px;font-size:17px}

.whats-new{left:0;top:893px;width:1200px;height:210px;background:var(--panel)}
.divider-h{left:233px;top:0;width:735px;border-top:1px dotted #8a7f70}
.whats-title{left:0;top:13px;width:1200px;text-align:center;font-family:'Montserrat',sans-serif;font-weight:700;font-size:21px;letter-spacing:.5px;color:var(--green)}
.new-photo{position:absolute}

.footer{left:0;top:1103px;width:1200px;height:67px;background:var(--footer);color:var(--white);font-size:12px}
.footer span{position:absolute;top:27px}
</style>
</head>
<body>

<header>
  <div class="abs brand"><span class="brand-dot"></span><span class="brand-name">Lorvane Swim Shop</span></div>
  <div class="abs header-login">LOGIN</div>
  <div class="abs search">Search</div>
  <svg class="abs search-icon" width="22" height="22" viewBox="0 0 22 22" aria-hidden="true">
    <circle cx="8.5" cy="8.5" r="6" fill="none" stroke="#111" stroke-width="3"/>
    <line x1="13" y1="13" x2="19" y2="19" stroke="#111" stroke-width="3.5" stroke-linecap="round"/>
  </svg>
</header>

<nav class="abs nav">
  <a style="left:271px">HOME</a>
  <a style="left:351px">ABOUT</a>
  <a style="left:446px">SERVICES</a>
  <a style="left:563px">PRODUCTS</a>
  <a style="left:691px">TESTIMONIALS</a>
  <a style="left:850px">CONTACT</a>
</nav>

<section class="abs hero" role="img" aria-label="Woman in a wide striped sun hat sitting on the beach facing the ocean"></section>
<div class="abs hero-title">Feel the heat</div>
<div class="abs btn shop-now">SHOP NOW</div>

<main>
  <div class="abs welcome-photo" role="img" aria-label="Woman in a white wrap walking along the shoreline"></div>
  <h1 class="abs welcome-title">Welcome to Lorvane Shop</h1>
  <p class="abs welcome-lead">Lorem ipsum dolor sit amet, consectetuer adipiscing elit,<br>ut laoreet dolore magna aliquam erat volutpat.</p>
  <p class="abs welcome-body">Ut wisi enim ad minim veniam, quis nostrud exerci tation ullamcorper suscipit lobortis nisl ut aliquip ex ea commodo consequat. Duis autem vel eum iriure dolor in hendrerit in vulputate velit esse molestie consequat, vel illum dolore eu feugiat nulla facilisis at vero eros et accumsan et iusto odio dignissim qui blandit praesent luptatum zzril delenit augue duis dolore te feugait nulla facilisi. Nam liber tempor cum</p>
  <div class="abs divider-v"></div>

  <aside class="abs login-panel">
    <h2 class="abs login-title">Login</h2>
    <span class="abs field-label" style="top:72px">Username</span>
    <div class="abs field" style="top:67px"></div>
    <span class="abs field-label" style="top:102px">Password</span>
    <div class="abs field" style="top:99px"></div>
    <div class="abs btn login-btn">LOGIN</div>
  </aside>
</main>

<section class="abs whats-new">
  <div class="abs divider-h"></div>
  <h2 class="abs whats-title">WHATS NEW</h2>
  <div class="new-photo" style="left:331px;top:53px;width:186px;height:123px;background:linear-gradient(180deg,#e8ecef 0%,#c9cfc9 55%,#f0f0ee 100%)" role="img" aria-label="Woman in a polka dot bikini leaning on a beach railing"></div>
  <div class="new-photo" style="left:553px;top:53px;width:183px;height:119px;background:linear-gradient(180deg,#c9d6de 0%,#d7c9bf 50%,#2f5fb0 100%)" role="img" aria-label="Woman in a pink bikini relaxing on a blue lounge chair with a drink"></div>
  <div class="new-photo" style="left:769px;top:50px;width:186px;height:123px;background:linear-gradient(180deg,#e4ecf1 0%,#cfdbe0 55%,#3d78b8 80%,#e9e6df 100%)" role="img" aria-label="Woman in a blue bikini holding a blue wrap on the beach"></div>
</section>

<footer class="abs footer">
  <span style="left:433px">Copyright 2014&nbsp; Lorvane</span>
  <span style="left:591px">Contact Us&nbsp; |&nbsp; Terms and Conditions</span>
</footer>

</body>
</html>
```